Brightwell Acupuncture Studio Website Design

We are working with Brightwell Acunpuncture Studio. They are a local Chinese medicine and acupuncture studio and in need of a new website design.

Some sites to use for inspiration:

https://marbleriveracupuncture.example
https://cedarglowacupuncture.example
https://quietharborclinic.example
https://emberfieldacupuncture.example
https://fernhollowclinic.example

Thank you for taking the time to consider designing a website for us. We are web developers based in Stockton, CA, USA. Most of our projects go through the same process. Understanding this process may help you win a project with us. We custom-code all of our websites in-house. We don’t have any requirements as to what tools you use for your design, but we prefer Figma files. For any design that we label as four-stars, we send it to the client for review. The client picks the final design they want us to use. Once we complete this process, we will continue to show additional clients all the four-star sites and purchase them later. Your designs will have multiple chances to sell. For better chances of success, we ask that you follow these guidelines.

IMAGES:
If you use any images or icons in the design, we ask that you have a link to the asset so we can purchase the image/icon. Most of the designs we submit do not have the customer’s images on them unless they have some great images. Be creative; show us the feeling you are trying to portray with your image choices. Use any royalty-free site you choose. We subscribe to Vantrel and mainly use their images, but we can purchase images outside of Vantrel.

PLEASE NOTE: we will not submit designs to clients with watermarks on the images.

FONTS:
We ask that you identify the fonts used in the design. This can be done in a message if you want. We typically use Google Fonts and Vantrel Fonts.

CONTENT:
We're always open to different content and ideas. We often submit designs with stock images so the client can see our vision. We typically take pictures after the website launch to use their images with our vision. Lorem Ipsum is fine for paragraphs, but we ask that you write the headers in correct English. We want to be able to show the vision and identify the sections of the website.

INSPIRATION:
We typically add a couple of links in the brief of websites we like to help you get started in your design.

REVISIONS:
We do not often ask for revisions of the designs unless we see something in the design that may not appeal to the client. If there are slight changes that we want to make, we do that in the development process.

FEEDBACK:
We rarely give feedback on designs during the design process. We are working on many website projects and do not have the time to provide feedback. We usually respond if your request is well thought out and asks specific questions, but a note asking “feedback, please” usually goes unanswered.

```html
<!DOCTYPE html>
<html lang="en">
<head>
<meta charset="utf-8">
<title>Brightwell Acupuncture Studio</title>
<link rel="stylesheet" href="https://fonts.googleapis.com/css2?family=Cormorant+Garamond:wght@400;500&family=Jost:wght@400;500;600&family=Marcellus&display=swap">
<style>
  :root{
    --coral:#e0655f;
    --coral-soft:#ecb4b1;
    --card:#dddcdb;
    --ink:#3b3836;
    --ink-soft:#5a5552;
    --hero-top:#e4e2df;
    --hero-bottom:#cfcac4;
    --header-bg:#dcdad7;
    --teal:#a8cfd1;
    --mist:#d3dcdc;
    --blush:#d8c4c7;
    --white:#ffffff;
  }
  *{box-sizing:border-box;margin:0;padding:0}
  html,body{width:1200px;height:675px;overflow:hidden;background:var(--white)}
  body{font-family:"Jost",sans-serif;color:var(--ink);position:relative}

  .site-header{position:absolute;top:0;left:0;width:1200px;height:56px;background:var(--header-bg);
    display:flex;align-items:center;justify-content:space-between;padding:0 60px}
  .brand{display:flex;align-items:center;gap:10px;font-family:"Jost",sans-serif;font-weight:600;font-size:19px;color:var(--ink)}
  .brand-dot{width:14px;height:14px;border-radius:50%;background:var(--coral)}
  .main-nav{display:flex;gap:26px;font-size:12px;color:var(--ink-soft)}

  .hero{position:absolute;top:56px;left:0;width:1200px;height:204px;
    background:linear-gradient(180deg,var(--hero-top) 0%,#dedad5 60%,var(--hero-bottom) 100%)}
  .hero-photo{position:absolute;right:0;top:0;width:520px;height:204px;
    background:linear-gradient(120deg,rgba(0,0,0,0) 0%,rgba(140,110,80,.25) 55%,rgba(70,60,55,.35) 100%)}
  .hero-quote{position:absolute;left:110px;top:26px;font-family:"Cormorant Garamond",serif;font-size:31px;line-height:1.25;color:var(--ink)}
  .hero-quote cite{display:block;font-style:normal;color:var(--coral);margin-top:4px;margin-left:10px}
  .hero-lead{position:absolute;left:0;width:1200px;top:162px;text-align:center;font-size:10.5px;font-weight:500;
    letter-spacing:.06em;color:var(--white);line-height:1.6}

  .services{position:absolute;top:260px;left:0;width:1200px;height:150px;background:var(--coral);text-align:center;color:var(--white)}
  .services h2{font-family:"Jost",sans-serif;font-weight:500;font-size:27px;margin-top:18px}
  .services p{font-size:10.5px;font-weight:500;letter-spacing:.06em;line-height:1.65;width:860px;margin:8px auto 0}

  .therapy-list{position:absolute;top:372px;left:185px;display:flex;gap:40px}
  .therapy-card{width:250px;height:150px;background:var(--card);text-align:center}
  .therapy-photo{height:56px}
  .therapy-card h3{font-family:"Marcellus",serif;font-weight:400;font-size:15px;letter-spacing:.16em;margin-top:14px;color:var(--ink)}
  .therapy-card p{font-size:10.5px;letter-spacing:.05em;line-height:1.55;width:180px;margin:8px auto 0;color:var(--ink)}

  .wellness-link{position:absolute;top:534px;left:185px;width:830px;height:28px;background:var(--coral-soft);
    font-family:"Marcellus",serif;font-size:15px;letter-spacing:.14em;color:var(--white);text-align:center;line-height:28px}

  .journey{position:absolute;top:574px;left:0;width:1200px;height:101px;
    background:linear-gradient(90deg,var(--blush) 0%,var(--mist) 35%,var(--teal) 100%)}
  .journey h2{position:absolute;left:380px;top:14px;font-family:"Jost",sans-serif;font-weight:400;font-size:26px;letter-spacing:.3em;color:var(--white);line-height:1.35}
  .journey h2 span{display:block;font-size:19px}
  .journey-frame{position:absolute;left:720px;top:60px;width:340px;height:40px;border-left:2px solid var(--white);border-bottom:2px solid var(--white)}
  .journey p{position:absolute;left:150px;top:60px;width:170px;font-size:12px;letter-spacing:.1em;color:var(--white);line-height:1.5}
  .journey-plant{position:absolute;right:0;top:10px;width:140px;height:91px;background:radial-gradient(circle at 70% 60%,#3e6a3a 0%,rgba(62,106,58,0) 70%)}
</style>
</head>
<body>
  <header class="site-header">
    <div class="brand"><span class="brand-dot"></span>Brightwell Acupuncture Studio</div>
    <nav class="main-nav">
      <span>Welcome</span><span>Healing Therapies</span><span>Our Approach</span><span>Appointments</span><span>Reach Us</span>
    </nav>
  </header>

  <section class="hero">
    <div class="hero-photo" role="img" aria-label="Bonsai tree and tea set on a wooden tea table"></div>
    <blockquote class="hero-quote">
      "Healing is a matter of time,<br>but it is sometimes also a matter of opportunity."
      <cite>— Master Lian Wei</cite>
    </blockquote>
    <p class="hero-lead">Lorem ipsum dolor sit amet, consectetur adipiscing elit. Mauris in sapien eget nulla ultrices fermentum. Suspendisse<br>sed ex non nunc ultricies feugiat. Integer vitae justo vitae lorem egestas consequat.</p>
  </section>

  <section class="services">
    <h2>Rooted in Tradition, Focused on You</h2>
    <p>Lorem ipsum dolor sit amet, consectetur adipiscing elit. In every session, we honor the ancient wisdom of Chinese medicine while addressing your unique wellness goals. From acupuncture to herbal healing, our treatments are designed to restore balance, vitality, and inner peace.</p>
  </section>

  <div class="therapy-list">
    <article class="therapy-card">
      <div class="therapy-photo" role="img" aria-label="Acupuncture needles on a treatment tray" style="background:linear-gradient(90deg,#8a6a55,#5a4a42)"></div>
      <h3>ACUPUNCTURE</h3>
      <p>Fine needles that restore flow and ease tension throughout the body.</p>
    </article>
    <article class="therapy-card">
      <div class="therapy-photo" role="img" aria-label="Bowls of dried herbs and tea" style="background:linear-gradient(90deg,#4a3e38,#2e2a28)"></div>
      <h3>HERBAL MEDICINE</h3>
      <p>Custom herbal blends to support the body's natural healing abilities.</p>
    </article>
    <article class="therapy-card">
      <div class="therapy-photo" role="img" aria-label="Smoking moxa stick on a dark wooden surface" style="background:linear-gradient(180deg,#6a6a70,#3a302c)"></div>
      <h3>MOXIBUSTION</h3>
      <p>Gentle therapies to promote circulation and relieve stagnation.</p>
    </article>
  </div>

  <div class="wellness-link">FOLLOW THE PATH TO WELLNESS →</div>

  <section class="journey" role="img" aria-label="Soft teal backdrop with a leafy green plant">
    <h2>YOUR HEALING JOURNEY<span>BEGINS HERE</span></h2>
    <p>Lorem ipsum dolor sit amet, consectetur</p>
    <div class="journey-frame"></div>
    <div class="journey-plant"></div>
  </section>
</body>
</html>
```